Landcape Construction Company needs a flyer to catch attention

A flyer that can be displayed at several different stores detailing our skills, work produced, experience and contact details. Information can be extracted from our website www.brvkw.co.nz. The flyer should feel very green, with addition of pics of work completed as well as stock images of lush green plants, lawns, landscape or similar. Needs to be eye catching with just enough information to express our experience and commitment to high standards

Target Market(s)

Residential
Landscape Architects

Industry/Entity Type

Landscaping

Font styles to use
Serif

Colors
abd037

Requirements
Must have
• Our logo
Experience
Services offered including pictures
All information avail on our website www.brvkw.co.nz
Nice to have
• stock images of lush greenery like a garden after fresh rainfall
Should not have
• Nothing comes to mind

```html
<!DOCTYPE html>
<html lang="en">
<head>
<meta charset="utf-8">
<title>The Kowhai Yard Company – Flyer</title>
<link href="https://fonts.googleapis.com/css2?family=Source+Sans+3:wght@300;400;700&display=swap" rel="stylesheet">
<style>
  :root{
    --backdrop:#f3f5ea;
    --paper:#ffffff;
    --lime:#8cc63f;
    --forest:#1a7a3c;
    --band:#137a44;
    --lawn:#5e9c35;
    --foliage:#3e7a34;
    --stone:#8d8f8c;
  }
  *{box-sizing:border-box;margin:0;padding:0}
  html,body{width:1200px;height:1200px;overflow:hidden;background:var(--backdrop)}
  body{position:relative;font-family:"Source Sans 3",Arial,sans-serif;color:var(--forest)}
  .page{position:absolute;background:var(--paper)}
  .page-front{left:117px;top:123px;width:451px;height:946px}
  .page-back{left:630px;top:123px;width:453px;height:953px}
  .abs{position:absolute}
  .panel{background:var(--lime);text-align:center;color:var(--forest)}
  .panel h2{color:#fff;font-weight:700;font-size:22px;letter-spacing:.3px;line-height:1}
  .panel p{font-weight:300;font-size:15.5px;line-height:19.2px;text-transform:uppercase}
  .about{left:20px;top:21px;width:244px;height:339px;padding:9px 10px 0}
  .about h2{margin-bottom:10px}
  .brand{left:300px;top:23px;width:140px;text-align:center}
  .brand-dot{width:83px;height:83px;border-radius:50%;background:var(--lime);margin:0 auto 7px}
  .brand-name{font-weight:700;font-size:12.5px;line-height:14px;color:var(--forest)}
  .photo{display:block}
  .hedge{left:283px;top:146px;width:148px;height:401px;background:linear-gradient(180deg,#6f9a55 0%,var(--foliage) 45%,#2f6a2c 70%,var(--lawn) 85%,#74b43c 100%)}
  .courtyard{left:20px;top:378px;width:245px;height:169px;background:linear-gradient(180deg,#b8c9a8 0%,#a8b59c 40%,#c9c1b2 70%,#b7a991 100%)}
  .experience{left:20px;top:563px;width:412px;height:323px;padding:9px 26px 0}
  .experience h2{margin-bottom:10px}
  .contact{left:20px;top:898px;width:412px;height:37px;background:var(--band);color:#fff;font-size:16px;line-height:37px;text-align:center}
  .contact b{color:var(--lime);font-weight:700}
  .service-list{left:21px;top:17px;list-style:none;font-size:16px;line-height:19.4px;text-transform:uppercase}
  .service-list li:nth-child(odd){color:var(--forest)}
  .service-list li:nth-child(even){color:var(--lime)}
  .services{left:212px;top:19px;width:225px;height:294px;padding:6px 6px 0}
  .services h2{margin-bottom:8px}
  .gallery-shot{top:330px;width:129px;height:103px}
  .g1{left:19px;background:linear-gradient(180deg,#3f7fd0 0%,#9cc2ea 45%,#f2f2f2 55%,#5fa23a 100%)}
  .g2{left:165px;background:linear-gradient(180deg,#7fa35a 0%,#c58a5e 45%,#efece4 65%,#9a6a44 100%)}
  .g3{left:309px;background:linear-gradient(180deg,#8fbde8 0%,#4d8a3a 40%,#6fb23c 100%)}
  .projects-title{left:0;top:446px;width:453px;text-align:center;color:var(--lime);font-weight:700;font-size:22px;letter-spacing:.3px}
  .proj{width:129px;height:103px}
  .col-a{left:19px}.col-b{left:165px}.col-c{left:309px}
  .r1{top:479px}.r2{top:597px}.r3{top:714px}.r4{top:833px}
  .label{background:var(--lime);color:#fff;font-weight:400;font-size:15.5px;text-transform:uppercase;text-align:center}
  .label span{position:absolute;left:0;width:100%}
  .label .top{top:24px}.label .bottom{top:61px}
  .label .top::before{content:"";position:absolute;left:0;top:5px;border-style:solid;border-width:5px 0 5px 6px;border-color:transparent transparent transparent #fff}
  .label .bottom::after{content:"";position:absolute;right:0;top:5px;border-style:solid;border-width:5px 6px 5px 0;border-color:transparent #fff transparent transparent}
  .street{background:linear-gradient(180deg,#9aa3a9 0%,#8e9094 40%,#b3b3b0 100%)}
  .gravel{background:linear-gradient(180deg,#8a8a86 0%,#7a6e5e 25%,#857966 100%)}
  .steps{background:linear-gradient(180deg,#6c7a72 0%,#8d8c87 45%,#4a4d47 75%,#5a8a3a 100%)}
  .tiles{background:linear-gradient(180deg,#9ea39a 0%,#6c7178 50%,#4e545c 100%)}
  .deck{background:linear-gradient(180deg,#6b4a34 0%,#b79b78 40%,#8a4a2e 100%)}
  .asphalt{background:linear-gradient(180deg,#8a7a74 0%,#5c5f63 35%,#4f5256 100%)}
  .pavers{background:linear-gradient(180deg,#d4d4d0 0%,#b2b0a8 45%,#9c9a95 100%)}
  .path{background:linear-gradient(180deg,#b7c2cc 0%,#7a5245 35%,#4c6a36 70%,#5f8a3c 100%)}
</style>
</head>
<body>

<section class="page page-front">
  <div class="abs panel about">
    <h2>ABOUT US</h2>
    <p>Our company is built on honesty, teamwork, sound knowledge and a determination to provide our customers with the highest quality product and service. We are a small team of highly skilled, dedicated and reliable professionals who complete projects efficiently and with outstanding workmanship.</p>
  </div>

  <div class="abs brand">
    <div class="brand-dot"></div>
    <div class="brand-name">The Kowhai Yard Company Ltd</div>
  </div>

  <div class="abs photo hedge" role="img" aria-label="Row of tall conifer trees above a lush green lawn"></div>
  <div class="abs photo courtyard" role="img" aria-label="Timber deck courtyard with outdoor table, chairs and potted shrubs"></div>

  <div class="abs panel experience">
    <h2>OUR EXPERIENCE</h2>
    <p>With more than 25 years experience in the landscaping industry, The Kowhai Yard Company offers services to large or small residential and commercial projects. Based in Canterbury, we are locally owned and operated. Whether you have a blank canvas or are looking to rejuvenate your property we are able to advise and make the process easy and stress free. From paving, pergolas and decks to concrete or planting your dream garden we have the expertise to help.</p>
  </div>

  <div class="abs contact"><b>Mobile:</b> 021 555 0142 | <b>Email:</b> mark@brvkw.co.nz</div>
</section>

<section class="page page-back">
  <ul class="abs service-list">
    <li>Patios</li><li>Paving</li><li>Concrete</li><li>Water Features</li><li>Decking</li><li>Fencing</li><li>Boardwalks</li><li>Timber</li><li>Planter Boxes</li><li>Pergolas</li><li>Retaining Walls</li><li>Gardens &amp; Lawns</li><li>Irrigation</li><li>Project Management</li><li>Consultation</li>
  </ul>

  <div class="abs panel services">
    <h2>SERVICES</h2>
    <p>As a full construction landscaping company, we formally offer the following services. However, we regularly work with clients who want something a little out of the box. If there is something in particular you are after, we are happy to discuss options with you.</p>
  </div>

  <div class="abs photo gallery-shot g1" role="img" aria-label="White picket fence beside a green lawn under blue sky"></div>
  <div class="abs photo gallery-shot g2" role="img" aria-label="Timber veranda deck with white railing and garden chairs"></div>
  <div class="abs photo gallery-shot g3" role="img" aria-label="Landscaped garden with curving lawn and shrubs"></div>

  <h2 class="abs projects-title">OUR PROJECTS</h2>

  <div class="abs photo proj col-a r1 street" role="img" aria-label="New paved streetscape footpath under construction"></div>
  <div class="abs proj col-b r1 label"><span class="top">Streetscapes</span><span class="bottom">Ashgrove</span></div>
  <div class="abs photo proj col-c r1 gravel" role="img" aria-label="Large levelled gravel site with a road cone"></div>

  <div class="abs photo proj col-a r2 steps" role="img" aria-label="Timber steps and platform beside a lawn"></div>
  <div class="abs proj col-b r2 label"><span class="top">Newbury</span><span class="bottom">Rangiora</span></div>
  <div class="abs photo proj col-c r2 tiles" role="img" aria-label="Dark tiled patio with outdoor seating and hedge planters"></div>

  <div class="abs photo proj col-a r3 deck" role="img" aria-label="Hardwood deck with built-in bench and slatted screen"></div>
  <div class="abs proj col-b r3 label"><span class="top">Birch Place</span><span class="bottom">Elmfield Street</span></div>
  <div class="abs photo proj col-c r3 asphalt" role="img" aria-label="Exposed aggregate concrete driveway in front of a house"></div>

  <div class="abs photo proj col-a r4 pavers" role="img" aria-label="Grey paver courtyard with timber table and bench"></div>
  <div class="abs proj col-b r4 label"><span class="top">Various</span><span class="bottom">Residential</span></div>
  <div class="abs photo proj col-c r4 path" role="img" aria-label="Stepping stone garden path between planted beds and brick walls"></div>
</section>

</body>
</html>
```